web page for "Policy Heritage Bureau"
Policy Heritage Bureau
Creative Brief
Corporate Services
policy-heritage.com
I have started a squarespace webpage that has most of what we will want on our webpage. we would like to use the logo on that page, and have the Background, Coverage Ledger Study, etc pages on it.
https://brent-hollis-72d4.pagecraftly.com/
we are looking for something that makes it look like we have been in business for a long time. the sort of classic banking website design. something that suggests long term stability, financial stability, historical document research.
apparently, dislikes include the page I designed on squarespace.
Traditional
something that says "your money is safe"
above header
http://www.kpvarden.com/
http://dulmetcover.com/servHistoric.html
http://usa.brillow.com/ProductsServices/BrillowSolutions/ID/8391/Global-Policy-Heritage-Bureau.a
Something to add. we are also looking for something that shows a combination of Private Investigation, and a Puzzle.

```html
<!DOCTYPE html>
<html lang="en">
<head>
<meta charset="utf-8">
<title>Policy Heritage Bureau</title>
<link rel="stylesheet" href="https://fonts.googleapis.com/css2?family=Tinos:ital,wght@0,400;0,700;1,400;1,700&family=Oswald:wght@400&display=swap">
<style>
  :root {
    --green: #669a00;
    --green-bright: #7ab200;
    --green-nav: #659800;
    --green-line: #78a823;
    --dark: #343434;
    --white: #ffffff;
    --ink: #1e1e1e;
    --body-ink: #3a3a3a;
    --muted: #8a8a8a;
    --photo-top: #8a8c88;
    --photo-mid: #6f716d;
    --photo-low: #5a5b57;
  }
  * { box-sizing: border-box; margin: 0; padding: 0; }
  html, body { width: 1200px; height: 729px; overflow: hidden; }
  body { font-family: "Tinos", "Times New Roman", serif; color: var(--white); }
  .page { position: relative; width: 1200px; height: 729px; overflow: hidden; }

  .hero-photo {
    position: absolute; inset: 0;
    background: linear-gradient(180deg, var(--photo-top) 0%, var(--photo-mid) 45%, var(--photo-low) 70%, #7a7a76 100%);
  }
  .top-bar {
    position: absolute; left: 0; top: 0; width: 1200px; height: 26px;
    background: rgba(50, 50, 50, 0.55);
  }
  .tagline {
    position: absolute; right: 180px; top: 5px;
    font-style: italic; font-weight: 700; font-size: 14px;
  }

  .sidebar { position: absolute; left: 173px; top: 0; width: 258px; }
  .brand {
    height: 144px; background: var(--white);
    display: flex; align-items: center; gap: 10px; padding-left: 14px;
  }
  .brand-mark { width: 26px; height: 26px; background: var(--green); flex: none; }
  .brand-name {
    font-size: 19px; line-height: 1.05; color: var(--ink); text-transform: uppercase;
  }
  .main-nav a {
    display: flex; align-items: center;
    padding-left: 28px; height: 42px;
    background: var(--green-nav); color: var(--white);
    text-decoration: none; font-size: 15px; text-transform: uppercase;
    border-bottom: 1px solid var(--green-line); line-height: 1.25;
  }
  .main-nav a.is-current { background: var(--green-bright); height: 41px; }
  .main-nav a.is-tall { height: 57px; }
  .contact-panel {
    background: var(--dark); height: 112px;
    border-bottom-right-radius: 44px;
    padding: 28px 0 0 26px; font-size: 14px;
  }
  .contact-panel p { display: flex; align-items: center; gap: 9px; margin-bottom: 15px; }
  .contact-panel .phone { font-size: 16px; }

  .testimonials {
    position: absolute; left: 173px; top: 505px; width: 258px; height: 207px;
    background: var(--dark); border-top-right-radius: 44px;
    padding: 12px 16px 0 18px;
  }
  .testimonials h2 {
    font-weight: 400; font-size: 21px; padding: 0 0 8px 2px;
    border-bottom: 1px solid #474747; margin-bottom: 10px;
  }
  .testimonials blockquote {
    font-style: italic; font-size: 12.5px; line-height: 1.37; color: #d4d4d4;
  }
  .testimonials .author {
    text-align: right; font-style: italic; font-weight: 700; font-size: 13px; margin-top: 3px; line-height: 1.3;
  }
  .testimonials .author .name { color: var(--green-bright); display: block; }
  .testimonials .author .role { color: var(--muted); display: block; }
  .slider-btn {
    position: absolute; bottom: 0; width: 27px; height: 27px;
    background: #222; display: flex; align-items: center; justify-content: center;
  }
  .slider-btn.prev { left: 0; }
  .slider-btn.next { right: 0; }

  .process-diagram { position: absolute; inset: 0; }
  .step-label { font-family: "Tinos", "Times New Roman", serif; font-size: 17px; fill: var(--white); }
  .step-number { font-family: "Tinos", "Times New Roman", serif; font-weight: 700; font-size: 15px; fill: var(--green); }
  .process-title { font-family: "Tinos", "Times New Roman", serif; font-weight: 700; font-size: 23px; fill: var(--white); }

  .welcome {
    position: absolute; left: 456px; top: 506px; width: 574px; height: 178px;
    background: var(--white); border-top-left-radius: 50px;
    padding: 20px 17px 0 20px; text-align: right;
  }
  .welcome h1 {
    font-weight: 400; font-size: 18.5px; color: var(--ink); text-transform: uppercase; margin-bottom: 8px;
  }
  .welcome p {
    font-size: 12.5px; line-height: 1.48; color: var(--body-ink); text-align: justify; text-align-last: right;
  }
  .read-more {
    display: inline-block; margin-top: 16px;
    font-family: "Oswald", "Arial Narrow", sans-serif; font-size: 14.5px; color: var(--green); text-decoration: none;
  }
  .copyright {
    position: absolute; right: 171px; top: 694px;
    font-weight: 700; font-size: 11px;
  }
</style>
</head>
<body>
<div class="page">
  <div class="hero-photo" role="img" aria-label="Photograph of a classical courthouse with columns and wide stone steps under an overcast sky"></div>

  <div class="top-bar"><p class="tagline">Insurance solutions for the modern world</p></div>

  <aside class="sidebar">
    <div class="brand">
      <span class="brand-mark"></span>
      <span class="brand-name">Policy Heritage<br>Bureau, LLC</span>
    </div>
    <nav class="main-nav">
      <a href="#" class="is-current">Home</a>
      <a href="#">Background</a>
      <a href="#">Process</a>
      <a href="#" class="is-tall">Coverage Ledger Study<br>&amp; Recovery</a>
      <a href="#">Testimonials</a>
    </nav>
    <div class="contact-panel">
      <p>
        <svg width="15" height="11" viewBox="0 0 15 11"><rect x="0" y="0" width="15" height="11" fill="#fff"/><path d="M0 0 L7.5 6 L15 0" fill="none" stroke="#343434" stroke-width="1.4"/></svg>
        info@policy-heritage.com
      </p>
      <p class="phone">
        <svg width="16" height="16" viewBox="0 0 24 24"><path fill="#fff" d="M6.6 10.8a15.1 15.1 0 0 0 6.6 6.6l2.2-2.2c.3-.3.7-.4 1-.2 1.1.4 2.3.6 3.6.6.6 0 1 .4 1 1V20c0 .6-.4 1-1 1A17 17 0 0 1 3 4c0-.6.4-1 1-1h3.5c.6 0 1 .4 1 1 0 1.3.2 2.5.6 3.6.1.3 0 .7-.2 1z"/></svg>
        555-014-2290
      </p>
    </div>
  </aside>

  <section class="testimonials">
    <h2>Testimonials</h2>
    <blockquote>"Lorem ipsum dolor sit amet, consectetuer adipiscing elit, sed diam nonummy nibh euismod tincidunt ut laoreet dolore Lorem ipsum dolor sit amet,"</blockquote>
    <p class="author"><span class="name">- Mark Dalton</span><span class="role">Director</span></p>
    <a class="slider-btn prev" href="#" aria-label="Previous"><svg width="10" height="14" viewBox="0 0 10 14"><path d="M8 1 L2 7 L8 13" fill="none" stroke="#fff" stroke-width="2"/></svg></a>
    <a class="slider-btn next" href="#" aria-label="Next"><svg width="10" height="14" viewBox="0 0 10 14"><path d="M2 1 L8 7 L2 13" fill="none" stroke="#fff" stroke-width="2"/></svg></a>
  </section>

  <svg class="process-diagram" width="1200" height="729" viewBox="0 0 1200 729">
    <defs>
      <marker id="arrow-head" markerWidth="8" markerHeight="8" refX="6" refY="4" orient="auto">
        <path d="M0 0 L7 4 L0 8" fill="none" stroke="#e8e8e8" stroke-width="1.2"/>
      </marker>
      <linearGradient id="process-photo" x1="0" y1="0" x2="0" y2="1">
        <stop offset="0" stop-color="#8b7663"/>
        <stop offset="1" stop-color="#5b5048"/>
      </linearGradient>
    </defs>

    <g fill="none" stroke="#e8e8e8" stroke-width="1.2" marker-end="url(#arrow-head)">
      <path d="M545 426 Q500 360 533 288"/>
      <path d="M563 256 Q565 180 626 146"/>
      <path d="M664 128 Q700 82 755 78"/>
      <path d="M826 55 Q885 30 918 66"/>
    </g>

    <g class="step">
      <circle cx="597" cy="433" r="43" fill="var(--green)" stroke="#fff" stroke-width="1.5"/>
      <g fill="#fff">
        <path d="M576 433 l8 -6 v4 h7 v4 h-7 v4 z"/>
        <path d="M618 433 l-8 -6 v4 h-7 v4 h7 v4 z"/>
        <path d="M597 412 l-6 8 h4 v7 h4 v-7 h4 z"/>
        <path d="M597 454 l-6 -8 h4 v-7 h4 v7 h4 z"/>
      </g>
      <circle cx="558" cy="411" r="14" fill="#fff"/>
      <text class="step-number" x="558" y="416" text-anchor="middle">1</text>
      <text class="step-label" x="651" y="427">Interviews With</text>
      <text class="step-label" x="651" y="446">Employees</text>
    </g>

    <g class="step">
      <circle cx="587" cy="298" r="43" fill="var(--green)" stroke="#fff" stroke-width="1.5"/>
      <circle cx="584" cy="296" r="12" fill="none" stroke="#fff" stroke-width="3"/>
      <path d="M593 305 L603 315" stroke="#fff" stroke-width="5" stroke-linecap="round"/>
      <path d="M576 300 L582 292 L587 298 L598 284" fill="none" stroke="#fff" stroke-width="2.5"/>
      <path d="M592 282 L600 282 L600 290" fill="none" stroke="#fff" stroke-width="2.5"/>
      <circle cx="551" cy="270" r="14" fill="#fff"/>
      <text class="step-number" x="551" y="275" text-anchor="middle">2</text>
      <text class="step-label" x="639" y="311">Research &amp;</text>
      <text class="step-label" x="639" y="330">Internal Reviews</text>
    </g>

    <g class="step">
      <circle cx="674" cy="172" r="43" fill="var(--green)" stroke="#fff" stroke-width="1.5"/>
      <rect x="661" y="156" width="24" height="32" fill="#fff"/>
      <rect x="667" y="153" width="12" height="6" fill="#fff" stroke="var(--green)" stroke-width="1.5"/>
      <g stroke="var(--green)" stroke-width="1.5"><path d="M665 166 h16 M665 171 h16 M665 176 h10"/></g>
      <path d="M676 186 L688 168" stroke="var(--green)" stroke-width="3"/>
      <circle cx="645" cy="137" r="14" fill="#fff"/>
      <text class="step-number" x="645" y="142" text-anchor="middle">3</text>
      <text class="step-label" x="670" y="238">Contact With</text>
      <text class="step-label" x="654" y="257">Accounting Firms</text>
    </g>

    <g class="step">
      <circle cx="800" cy="101" r="43" fill="var(--green)" stroke="#fff" stroke-width="1.5"/>
      <rect x="781" y="89" width="38" height="26" rx="2" fill="#fff"/>
      <rect x="795" y="85" width="10" height="7" fill="#fff" stroke="var(--green)" stroke-width="1.5"/>
      <rect x="785" y="95" width="11" height="14" fill="var(--green)"/>
      <g stroke="var(--green)" stroke-width="2"><path d="M800 98 h14 M800 103 h14 M800 108 h10"/></g>
      <circle cx="772" cy="69" r="14" fill="#fff"/>
      <text class="step-number" x="772" y="74" text-anchor="middle">4</text>
      <text class="step-label" x="752" y="168">Contact With</text>
      <text class="step-label" x="774" y="187">Brokers</text>
    </g>

    <g class="step">
      <circle cx="957" cy="114" r="43" fill="var(--green)" stroke="#fff" stroke-width="1.5"/>
      <circle cx="955" cy="116" r="13" fill="none" stroke="#fff" stroke-width="3.5"/>
      <circle cx="955" cy="116" r="5" fill="#fff"/>
      <path d="M955 116 L970 101" stroke="#fff" stroke-width="3"/>
      <path d="M967 98 L974 96 L972 103" fill="#fff"/>
      <circle cx="934" cy="77" r="14" fill="#fff"/>
      <text class="step-number" x="934" y="82" text-anchor="middle">5</text>
      <text class="step-label" x="915" y="183">Conditions</text>
      <text class="step-label" x="906" y="202">For Policies</text>
    </g>

    <g class="process-badge">
      <circle cx="908" cy="350" r="101" fill="url(#process-photo)" stroke="#fff" stroke-width="7" role="img" aria-label="Photograph of ancient stone ruins"/>
      <text class="process-title" x="908" y="328" text-anchor="middle">The Process</text>
      <text class="process-title" x="908" y="354" text-anchor="middle">of</text>
      <text class="process-title" x="908" y="380" text-anchor="middle">Archaelogical</text>
      <text class="process-title" x="908" y="406" text-anchor="middle">Insurance</text>
    </g>
  </svg>

  <section class="welcome">
    <h1>Welcome to Policy Heritage Bureau</h1>
    <p>Lorem ipsum dolor sit amet, consectetuer adipiscing elit, sed diam nonummy nibh euismod tincidunt ut laoreet dolore magna aliquam erat volutpat. Ut wisi enim ad minim veniam, quis nostrud exerci tation ullamcorper suscipit lobortis nisl ut aliquip ex ea commodo consequat. Duis autem vel eum iriure dolor in hendrerit in vulputate velit esse molestie consequat.</p>
    <a class="read-more" href="#">Read More...</a>
  </section>

  <p class="copyright">Copyright 2015 Policy Heritage Bureau, LLC | All Rights Reserved.</p>
</div>
</body>
</html>
```